Vorquel 820 practise with the goal to have business and people Lifted past the horizon

We need a logo design for business cards for a company based in Australia Called TALBrookWare. We specialise in cloud tech from th full Quenfield stack. i would like it to be close to quenfield colours and we specilise in Quenfield Vorquel 820 Client Outreach. the design should display the confidence an security of a cloud based company. the tag line of Lifted past the horizon in the company motto.

Target Market(s)

I am targeting small to medium business up to 250 staff. i do work for not for profit and standard business.

Industry/Entity Type

Professional Service

Contact Information for Business Card

TALBrookWare Pty Ltd
A.C.N. 47 218 390 516
PO Box 827
Wattlemere 4177
Mobile: 0400382957
Email: Dermot@Talbrookware.example.com.au

Font styles to use
Sans Serif

Colors

Designer to choose colors to be used in the design.

Requirements
Must have
• as a cloud based business it needs to have the this as the main theme. the tag line of Liftedpast the horizon should show we look at empowering business to get the most out of the cloud to minimise the spend they have as the target for the business is business and not for profits who need the make the most of their spend.
• the attached pictures are to be a source of insperation and key areas
Nice to have
• Quenfield Vorquel 820 is the core product that we sell and implentent for our clients so the theme should complement the Quenfield Vorquel theme

```html
<!DOCTYPE html>
<html lang="en">
<head>
<meta charset="utf-8">
<title>TALBrookWare Business Card</title>
<link rel="stylesheet" href="https://fonts.googleapis.com/css2?family=Outfit:wght@400;500&display=swap">
<style>
  :root {
    --backdrop: #cfcfcf;
    --card-paper: #e6e6e6;
    --navy: #3b4a68;
    --sky-blue: #6d82b3;
    --brand-ink: #1f2a6e;
    --light-text: #f2f3f6;
  }
  html, body {
    margin: 0;
    padding: 0;
    width: 1200px;
    height: 1200px;
    overflow: hidden;
    background: var(--backdrop);
    font-family: "Outfit", sans-serif;
  }
  .canvas {
    position: relative;
    width: 1200px;
    height: 1200px;
  }
  .card {
    position: absolute;
    top: 278px;
    width: 369px;
    height: 646px;
    background: var(--card-paper);
    overflow: hidden;
  }
  .card--front { left: 218px; }
  .card--back { left: 613px; }
  .card-shapes {
    position: absolute;
    inset: 0;
  }
  .shape-navy { fill: var(--navy); }
  .shape-sky { fill: var(--sky-blue); }
  .brand {
    position: absolute;
    left: 64px;
    display: flex;
    align-items: center;
    gap: 14px;
  }
  .card--front .brand { top: 128px; }
  .card--back .brand { top: 302px; }
  .brand-mark {
    width: 30px;
    height: 30px;
    background: var(--brand-ink);
  }
  .brand-name {
    font-size: 27px;
    font-weight: 500;
    color: var(--brand-ink);
    letter-spacing: 0.2px;
  }
  .contact {
    position: absolute;
    left: 69px;
    top: 420px;
    color: var(--light-text);
  }
  .contact-company {
    margin: 0 0 14px;
    font-size: 16px;
    font-weight: 400;
  }
  .contact-lines {
    margin: 0 0 16px;
    font-size: 12px;
    line-height: 16px;
  }
  .contact-lines:last-child { margin-bottom: 0; font-size: 11.5px; }
</style>
</head>
<body>
<main class="canvas">
  <section class="card card--front">
    <svg class="card-shapes" viewBox="0 0 369 646" width="369" height="646" aria-hidden="true">
      <polygon class="shape-navy" points="0,362 196,294 330,314 347,337 334,562 369,646 0,646"/>
      <polygon class="shape-sky" points="369,0 369,646 334,562 347,337"/>
    </svg>
    <div class="brand">
      <span class="brand-mark"></span>
      <span class="brand-name">TALBrookWare</span>
    </div>
    <div class="contact">
      <p class="contact-company">TALBrookWare Pty Ltd</p>
      <p class="contact-lines">A.C.N. 47 218 390 516<br>PO Box 827<br>Wattlemere 4177</p>
      <p class="contact-lines">Mobile: 0400382957<br>Email: Dermot@Talbrookware.example.com.au</p>
    </div>
  </section>

  <section class="card card--back">
    <svg class="card-shapes" viewBox="0 0 369 646" width="369" height="646" aria-hidden="true">
      <polygon class="shape-navy" points="0,634 258,597 357,615 369,646 0,646"/>
      <polygon class="shape-sky" points="369,0 369,646 333,562"/>
    </svg>
    <div class="brand">
      <span class="brand-mark"></span>
      <span class="brand-name">TALBrookWare</span>
    </div>
  </section>
</main>
</body>
</html>
```